Business Card Design Project

Personal Service. There are three areas of my service: Resourceful/Recycling Consultation, Life Coaching using Law of Attraction & Visualization Board. My current cards has: Imagine Into Being. I would like to work with this theme

Industry/Entity Type

Business

Contact Information for Business Card

Circles. Recyling Triangle

```html
<!DOCTYPE html>
<html lang="en">
<head>
<meta charset="utf-8">
<title>Imagine Into Being – Business Card</title>
<link rel="stylesheet" href="https://fonts.googleapis.com/css2?family=Michroma&family=Source+Sans+3:wght@400;600&display=swap">
<style>
  :root {
    --page: #f4f5f7;
    --card-black: #030507;
    --glow-blue: #7fd8ff;
    --bar-core: #f2fdff;
    --tagline-green: #1f8a5c;
    --text-light: #e6f4ff;
    --text-soft: #c9d6df;
  }
  * { box-sizing: border-box; margin: 0; padding: 0; }
  html, body {
    width: 1200px; height: 900px; overflow: hidden;
    background: var(--page);
  }
  .card {
    position: absolute; left: 100px; top: 165px;
    width: 1000px; height: 570px;
    border-radius: 40px; overflow: hidden;
    background: var(--card-black);
    box-shadow: 0 18px 40px rgba(0,0,0,0.25);
  }
  .space-art {
    position: absolute; inset: 0;
    background:
      radial-gradient(ellipse 45% 10% at 55% 52%, rgba(60,190,220,0.55), transparent 70%),
      radial-gradient(ellipse 35% 14% at 78% 50%, rgba(40,150,90,0.45), transparent 70%),
      radial-gradient(ellipse 30% 12% at 30% 54%, rgba(30,110,170,0.45), transparent 70%),
      radial-gradient(ellipse 70% 40% at 50% 50%, rgba(20,50,70,0.5), transparent 75%),
      var(--card-black);
  }
  .brand-mark {
    position: absolute; left: 470px; top: 90px;
    width: 60px; height: 60px; border-radius: 50%;
    border: 4px solid var(--glow-blue);
    box-shadow: 0 0 16px rgba(127,216,255,0.8);
  }
  .brand {
    position: absolute; left: 0; right: 0; top: 215px;
    text-align: center; white-space: nowrap;
    font-family: "Michroma", sans-serif;
    font-size: 27px; font-weight: 400; letter-spacing: 1px;
    color: var(--text-light);
    text-shadow: 0 0 8px rgba(127,216,255,0.7);
  }
  .light-bar {
    position: absolute; left: 0; right: 20px; top: 270px;
    height: 22px; border-radius: 0 4px 4px 0;
    background: var(--bar-core);
    box-shadow: 0 0 14px 4px rgba(127,216,255,0.9), 0 0 40px 10px rgba(60,170,230,0.5);
  }
  .tagline {
    position: absolute; left: 0; right: 20px; top: 270px;
    height: 22px; line-height: 22px;
    text-align: center; white-space: nowrap;
    font-family: "Michroma", sans-serif;
    font-size: 13px; letter-spacing: 34px;
    padding-left: 34px;
    color: var(--tagline-green);
  }
  .person {
    position: absolute; right: 540px; top: 380px; text-align: right;
    font-family: "Source Sans 3", sans-serif;
  }
  .person-name {
    font-size: 32px; font-weight: 600; color: var(--text-light);
    text-shadow: 0 0 6px rgba(127,216,255,0.6);
  }
  .person-role { font-size: 19px; color: var(--text-soft); }
  .divider {
    position: absolute; left: 488px; top: 340px;
    width: 2px; height: 160px; background: var(--text-soft);
  }
  .contact {
    position: absolute; left: 512px; top: 348px;
    list-style: none;
    font-family: "Source Sans 3", sans-serif;
    font-size: 21px; line-height: 29px;
    color: var(--text-light);
    text-shadow: 0 0 6px rgba(127,216,255,0.6);
  }
  .contact li { display: flex; align-items: flex-start; gap: 6px; white-space: nowrap; }
  .contact svg { width: 22px; height: 22px; margin-top: 4px; flex: none; fill: var(--text-light); }
</style>
</head>
<body>
  <div class="card">
    <div class="space-art" role="img" aria-label="Starry deep-space nebula in teal and green across the card"></div>
    <div class="brand-mark"></div>
    <h1 class="brand">IMAGINE INTO BEING</h1>
    <div class="light-bar"></div>
    <p class="tagline">PERSONAL SERVICE</p>

    <div class="person">
      <p class="person-name">Rowan Ellery</p>
      <p class="person-role">Manager</p>
    </div>
    <div class="divider"></div>

    <ul class="contact">
      <li>
        <svg viewBox="0 0 24 24" aria-hidden="true"><path d="M6.6 10.8a15 15 0 0 0 6.6 6.6l2.2-2.2a1 1 0 0 1 1-.25 11.4 11.4 0 0 0 3.6.6 1 1 0 0 1 1 1V20a1 1 0 0 1-1 1A17 17 0 0 1 3 4a1 1 0 0 1 1-1h3.5a1 1 0 0 1 1 1c0 1.25.2 2.45.6 3.6a1 1 0 0 1-.25 1z"/></svg>
        <span>555-014-2287</span>
      </li>
      <li>
        <svg viewBox="0 0 24 24" aria-hidden="true"><path d="M3 5h18a1 1 0 0 1 1 1v12a1 1 0 0 1-1 1H3a1 1 0 0 1-1-1V6a1 1 0 0 1 1-1zm1 2.2V17h16V7.2l-8 5.3z M5 7l7 4.6L19 7z"/></svg>
        <span>info@imagineintobeing.com</span>
      </li>
      <li>
        <svg viewBox="0 0 24 24" aria-hidden="true" fill="none"><g stroke="#e6f4ff" stroke-width="1.6" fill="none"><circle cx="12" cy="12" r="9"/><ellipse cx="12" cy="12" rx="4" ry="9"/><path d="M3 12h18M4.5 7.5h15M4.5 16.5h15"/></g></svg>
        <span>www.imagineintobeing.com</span>
      </li>
      <li>
        <svg viewBox="0 0 24 24" aria-hidden="true"><path d="M12 3l10 9h-3v9h-5v-6h-4v6H5v-9H2z"/></svg>
        <span>4820 N. Meadow Road,<br>Fairview, Texas 75069</span>
      </li>
    </ul>
  </div>
</body>
</html>
```